stars + comments Reviews website design (similar to quarn concept)

Please refer to attached logo and wire frames
----------------------------------------------------------------------------------------------------
we are a company based in egypt, seeking a design for a website that allows user to find doctors using search and filters.
also it allows user to review this doctor through providing comment and 1 to 5 stars
i need 4 main pages designs:
1- Doctors list/favorites list
2- Doctor view
3- Add doctor (3 steps)
4- Sign-in/sign up
5- Menu design
am into the colors teal/turquoise (though am open for different opinion)
i don't want the design theme to be doctors specific
am into the school of very clean, very neat, very simple
(plombex, ruvanteo, melvoshade designs are appealing to me)

Number of Pages Required

4 page

Font styles to use
Sans Serif

Colors
00a990
33b8a4

Requirements
Must have
• website will be bilingual/ bi-directional (English and Arabic)
• designer needs to provide another copy of the design with "right to left" orientation
• interactive button animation

```html
<!DOCTYPE html>
<html lang="en">
<head>
<meta charset="utf-8">
<title>Ratevia – Doctors</title>
<link rel="stylesheet" href="https://fonts.googleapis.com/css2?family=Arimo:wght@400;700&family=Roboto+Slab:wght@400&family=Roboto+Condensed:wght@400&display=swap">
<style>
  :root{
    --teal:#00979b;
    --teal-soft:#33b8a4;
    --ink:#2b2b2b;
    --ink-dark:#333;
    --rule:#e6e6e6;
    --white:#fff;
    --photo-a:#e9ecee;
    --photo-b:#33465e;
  }
  *{box-sizing:border-box;margin:0;padding:0}
  html,body{width:1130px;height:1200px;overflow:hidden;background:var(--white)}
  body{position:relative;font-family:"Arimo",Arial,sans-serif;color:var(--ink)}

  .top-band{position:absolute;left:0;top:0;width:1130px;height:14px;background:var(--teal)}
  .top-rule{position:absolute;left:0;top:17px;width:1130px;height:3px;background:var(--ink-dark)}

  .brand{position:absolute;left:40px;top:5px;width:302px;height:107px;background:var(--teal);border:4px solid var(--white);outline:0;display:flex;align-items:center;justify-content:center;gap:12px}
  .brand-mark{width:30px;height:30px;background:var(--white)}
  .brand-name{font-family:"Arimo",Arial,sans-serif;font-weight:700;font-size:46px;color:var(--white);letter-spacing:.5px}

  .main-nav{position:absolute;top:58px;left:0;width:1130px;height:52px}
  .nav-item{position:absolute;display:flex;flex-direction:column;align-items:center;font-family:"Roboto Slab",Georgia,serif;font-size:14px;color:var(--ink);text-decoration:none;transform:translateX(-50%)}
  .nav-item svg{height:30px;margin-bottom:4px}
  .nav-item.is-active{color:var(--teal)}
  .nav-home{left:458px}
  .nav-share{left:562px}
  .nav-doctors{left:692px}

  .user-button{position:absolute;left:983px;top:76px;width:106px;height:33px;background:var(--teal);color:var(--white);font-size:15px;display:flex;align-items:center;justify-content:center}

  .header-rule{position:absolute;left:42px;top:119px;width:1047px;height:1px;background:var(--rule)}

  .filters{position:absolute;top:133px;left:0;width:1130px;height:43px}
  .filter{position:absolute;top:0;height:43px;border:2px solid var(--teal);display:flex;align-items:center;font-size:14px;color:var(--ink)}
  .filter-label{flex:1;padding-left:10px}
  .filter-toggle{width:34px;height:100%;border-left:2px solid var(--teal);display:flex;align-items:center;justify-content:center;font-size:14px}
  .f-search{left:42px;width:214px}
  .f-spec{left:270px;width:148px}
  .f-sub{left:432px;width:168px}
  .f-area{left:615px;width:149px}
  .f-gender{left:777px;width:149px}
  .f-rating{left:940px;width:149px}
  .f-search .filter-toggle svg{width:20px;height:20px}

  .filters-rule{position:absolute;left:42px;top:188px;width:1047px;height:1px;background:var(--rule)}

  .result-count{position:absolute;left:78px;top:215px;font-family:"Roboto Condensed",Arial,sans-serif;font-size:20px;color:var(--teal)}

  .doctor-list{position:absolute;left:42px;top:251px;width:1047px;height:876px;border:1px solid var(--teal);list-style:none}
  .doctor{position:absolute;left:33px;width:982px;height:160px;border-bottom:3px solid var(--rule)}
  .doctor-photo{position:absolute;left:0;top:0;width:132px;height:116px;background:linear-gradient(135deg,var(--photo-a) 0%,var(--photo-a) 35%,var(--photo-b) 75%);border:1px solid var(--rule)}
  .doctor-info{position:absolute;left:155px;top:9px;font-family:"Roboto Slab",Georgia,serif;font-size:15px;line-height:24px;color:var(--ink)}
  .doctor-name{color:var(--teal-soft)}
  .doctor-rating{position:absolute;left:762px;top:5px;display:flex;gap:8px}
  .doctor-rating svg{width:24px;height:24px}
  .star-on{fill:var(--teal)}
  .star-off{fill:var(--ink-dark)}
  .review-count{position:absolute;left:934px;top:6px;font-family:"Roboto Slab",Georgia,serif;font-size:19px;color:var(--ink-dark)}
  .doctor-fav{position:absolute;left:886px;top:46px;width:24px;height:24px}
  .fav-off{fill:#000}
  .fav-on{fill:var(--teal-soft)}

  .site-footer{position:absolute;left:0;top:1159px;width:1130px;height:41px;background:var(--teal-soft);display:flex;align-items:center;justify-content:center;font-size:13px;color:#111}
</style>
</head>
<body>
<svg width="0" height="0" style="position:absolute">
  <defs>
    <symbol id="i-star" viewBox="0 0 24 24"><path d="M12 1.5l3.1 7 7.4.6-5.6 4.9 1.7 7.4L12 17.5l-6.6 3.9 1.7-7.4L1.5 9.1l7.4-.6z"/></symbol>
    <symbol id="i-heart" viewBox="0 0 24 24"><path d="M12 22S1.5 14.5 1.5 7.6C1.5 4.4 3.9 2 6.9 2c2.1 0 3.9 1.2 5.1 3 1.2-1.8 3-3 5.1-3 3 0 5.4 2.4 5.4 5.6C22.5 14.5 12 22 12 22z"/></symbol>
  </defs>
</svg>

<div class="top-band"></div>
<div class="top-rule"></div>

<header>
  <div class="brand"><span class="brand-mark"></span><span class="brand-name">Ratevia</span></div>

  <nav class="main-nav">
    <a class="nav-item nav-home is-active" href="#">
      <svg viewBox="0 0 30 30" width="30"><path d="M15 3L2 15h4v12h7v-8h4v8h7V15h4z" fill="var(--teal)"/></svg>Home
    </a>
    <a class="nav-item nav-share" href="#">
      <svg viewBox="0 0 24 24" width="28"><use href="#i-heart" fill="#000"/></svg>Share
    </a>
    <a class="nav-item nav-doctors" href="#">
      <svg viewBox="0 0 30 30" width="30"><circle cx="15" cy="9" r="6" fill="#9a9a9a"/><path d="M4 29c0-7 5-11 11-11s11 4 11 11z" fill="#6d6d6d"/><rect x="13.5" y="19" width="3" height="7" fill="#fff"/></svg>List of Doctors
    </a>
  </nav>

  <div class="user-button">Omar Lane</div>
</header>

<div class="header-rule"></div>

<form class="filters">
  <div class="filter f-search"><span class="filter-label">Search</span><span class="filter-toggle"><svg viewBox="0 0 20 20"><circle cx="8" cy="8" r="5.5" fill="none" stroke="var(--teal)" stroke-width="2"/><path d="M12 12l6 6" stroke="var(--teal)" stroke-width="2.5"/></svg></span></div>
  <div class="filter f-spec"><span class="filter-label">Specialization</span><span class="filter-toggle">v</span></div>
  <div class="filter f-sub"><span class="filter-label" style="padding-left:6px">Sub-Specialization</span><span class="filter-toggle">v</span></div>
  <div class="filter f-area"><span class="filter-label">Area</span><span class="filter-toggle">v</span></div>
  <div class="filter f-gender"><span class="filter-label">Gender</span><span class="filter-toggle">v</span></div>
  <div class="filter f-rating"><span class="filter-label">Rating</span><span class="filter-toggle">v</span></div>
</form>

<div class="filters-rule"></div>

<h2 class="result-count">15,123 Doctors</h2>

<ul class="doctor-list">
  <li class="doctor" style="top:23px">
    <div class="doctor-photo" role="img" aria-label="Portrait photo of the doctor"></div>
    <div class="doctor-info"><span class="doctor-name">Karim Fathy</span> (1 Km Away)<br>Anesthesiologist<br>18 Sarwat Lane, Westbrook</div>
    <div class="doctor-rating"><svg class="star-on"><use href="#i-star"/></svg><svg class="star-on"><use href="#i-star"/></svg><svg class="star-on"><use href="#i-star"/></svg><svg class="star-on"><use href="#i-star"/></svg><svg class="star-off"><use href="#i-star"/></svg></div>
    <span class="review-count">(123)</span>
    <svg class="doctor-fav fav-off"><use href="#i-heart"/></svg>
  </li>
  <li class="doctor" style="top:183px">
    <div class="doctor-photo" role="img" aria-label="Portrait photo of the doctor"></div>
    <div class="doctor-info"><span class="doctor-name">Karim Fathy</span> (1 Km Away)<br>Anesthesiologist<br>18 Sarwat Lane, Westbrook</div>
    <div class="doctor-rating"><svg class="star-on"><use href="#i-star"/></svg><svg class="star-on"><use href="#i-star"/></svg><svg class="star-on"><use href="#i-star"/></svg><svg class="star-on"><use href="#i-star"/></svg><svg class="star-off"><use href="#i-star"/></svg></div>
    <span class="review-count">(123)</span>
    <svg class="doctor-fav fav-on"><use href="#i-heart"/></svg>
  </li>
  <li class="doctor" style="top:344px">
    <div class="doctor-photo" role="img" aria-label="Portrait photo of the doctor"></div>
    <div class="doctor-info"><span class="doctor-name">Karim Fathy</span> (1 Km Away)<br>Anesthesiologist<br>18 Sarwat Lane, Westbrook</div>
    <div class="doctor-rating"><svg class="star-on"><use href="#i-star"/></svg><svg class="star-on"><use href="#i-star"/></svg><svg class="star-on"><use href="#i-star"/></svg><svg class="star-on"><use href="#i-star"/></svg><svg class="star-off"><use href="#i-star"/></svg></div>
    <svg class="doctor-fav fav-off"><use href="#i-heart"/></svg>
  </li>
  <li class="doctor" style="top:505px">
    <div class="doctor-photo" role="img" aria-label="Portrait photo of the doctor"></div>
    <div class="doctor-info"><span class="doctor-name">Karim Fathy</span> (1 Km Away)<br>Anesthesiologist<br>18 Sarwat Lane, Westbrook</div>
    <div class="doctor-rating"><svg class="star-on"><use href="#i-star"/></svg><svg class="star-on"><use href="#i-star"/></svg><svg class="star-on"><use href="#i-star"/></svg><svg class="star-on"><use href="#i-star"/></svg><svg class="star-off"><use href="#i-star"/></svg></div>
    <svg class="doctor-fav fav-off"><use href="#i-heart"/></svg>
  </li>
  <li class="doctor" style="top:666px">
    <div class="doctor-photo" role="img" aria-label="Portrait photo of the doctor"></div>
    <div class="doctor-info"><span class="doctor-name">Karim Fathy</span> (1 Km Away)<br>Anesthesiologist<br>18 Sarwat Lane, Westbrook</div>
    <div class="doctor-rating"><svg class="star-on"><use href="#i-star"/></svg><svg class="star-on"><use href="#i-star"/></svg><svg class="star-on"><use href="#i-star"/></svg><svg class="star-on"><use href="#i-star"/></svg><svg class="star-off"><use href="#i-star"/></svg></div>
    <svg class="doctor-fav fav-on"><use href="#i-heart"/></svg>
  </li>
</ul>

<footer class="site-footer">Copyright ©2015 Ratevia&nbsp; All Rights Reserved</footer>
</body>
</html>
```